Franchise Vacation Rental Company Website

We are looking for fresh, new and creative design ideas to help enhance this site. We are a vacation rental company that is starting a new franchise business. This will be our home franchise page, and will need to appeal to franchise candidates as well as travelers looking for vacation homes in our current locations.

Business

```html
<!DOCTYPE html>
<html lang="en">
<head>
<meta charset="utf-8">
<title>BaySide Stays – Find Your Spot</title>
<link href="https://fonts.googleapis.com/css2?family=Open+Sans:wght@400;600;700&display=swap" rel="stylesheet">
<style>
:root{
  --blue:#1a73bf;
  --lime:#a4c639;
  --lime-dark:#8fb12a;
  --ink:#222;
  --link:#1a73bf;
  --page:#efefef;
  --panel:#fff;
  --footer:#f6f6f6;
  --line:#e4e4e4;
  --sky:#1aa0d8;
}
*{box-sizing:border-box;margin:0;padding:0}
html,body{width:814px;height:1200px;overflow:hidden}
body{position:relative;font-family:"Open Sans",Arial,sans-serif;color:var(--ink);background:var(--page)}
.abs{position:absolute}
.header{left:0;top:0;width:814px;height:91px;background:var(--blue)}
.brand{left:117px;top:30px;font-size:25px;font-weight:400;color:#c6e05a}
.contact-top{right:115px;top:16px;text-align:right;color:#fff}
.contact-top .mail{font-size:9px;display:flex;align-items:center;gap:6px;justify-content:flex-end}
.contact-top .phone{font-size:14px;margin-top:9px}
.contact-top .phone-num{font-size:10px;margin-top:3px}
.nav{left:0;top:91px;width:814px;height:35px;background:var(--lime);border-bottom:2px solid #93b52c}
.nav .home{position:absolute;left:118px;top:0;width:54px;height:33px;background:var(--blue);display:flex;align-items:center;justify-content:center}
.nav a{position:absolute;top:0;height:33px;line-height:33px;font-size:8.6px;font-weight:600;color:#fff;text-decoration:none}
.nav .sep{position:absolute;top:0;width:1px;height:33px;background:#b7d650}
.intro{left:0;top:126px;width:814px;height:76px;background:#fff}
.intro h1{position:absolute;left:139px;top:19px;font-size:16px;font-weight:600;color:var(--blue)}
.intro p{position:absolute;left:140px;top:47px;font-size:8px;color:#333}
.share{position:absolute;left:630px;top:32px;display:flex;gap:4px}
.share span{width:12px;height:12px;border-radius:2px}
.share .count{width:14px;background:#fff;border:1px solid #ccc;font-size:6px;text-align:center;line-height:10px;color:#666}
.tile{width:179px;height:135px;background:#fff;padding:2px;box-shadow:0 0 2px rgba(0,0,0,.15)}
.tile .photo{width:100%;height:100%;position:relative;overflow:hidden}
.tile .label{position:absolute;left:0;bottom:0;width:100%;height:26px;background:rgba(0,0,0,.35);color:#fff;text-align:center;font-size:12px;line-height:26px}
.join .photo{background:linear-gradient(#555d64,#454c46)}
.join h2{position:absolute;width:100%;top:16px;text-align:center;font-size:14px;font-weight:600;color:#fff}
.join p{position:absolute;width:100%;top:44px;text-align:center;font-size:8px;line-height:17px;color:#fff}
.join .btn{position:absolute;left:40px;top:87px;width:95px;height:28px;background:var(--lime);color:#fff;font-size:10.5px;font-weight:600;text-align:center;line-height:28px;border-radius:2px}
.panel{left:117px;top:546px;width:581px;height:404px;background:var(--panel)}
.story{position:absolute;left:17px;top:20px;width:260px}
.story h3{font-size:10.5px;font-weight:400;color:var(--blue)}
.story h4{font-size:9.5px;font-weight:400;margin-top:13px}
.story p{font-size:6.9px;line-height:12.8px;text-align:justify;color:#333;margin-top:14px}
.story p+p{margin-top:21px}
.story .more{position:absolute;left:1px;top:352px;width:55px;height:24px;background:linear-gradient(#b6d64a,var(--lime-dark));color:#fff;font-size:7px;text-align:center;line-height:24px}
.divider{position:absolute;left:301px;top:28px;width:1px;height:350px;background:linear-gradient(transparent,#e6e6e6 20%,#e6e6e6 80%,transparent)}
.signup{position:absolute;left:325px;top:21px;width:243px;height:91px;border:1px solid var(--line)}
.signup h3{position:absolute;left:17px;top:12px;font-size:11.5px;font-weight:400}
.signup .field{position:absolute;left:17px;top:42px;width:136px;height:31px;border:1px solid #ddd;font-size:7px;line-height:29px;padding-left:10px;color:#333}
.signup .go{position:absolute;left:161px;top:42px;width:64px;height:31px;background:var(--blue);color:#fff;font-size:11px;text-align:center;line-height:31px;border-radius:2px}
.feature{position:absolute;left:325px;width:243px;height:77px}
.feature .icon{position:absolute;left:0;top:0;width:44px;height:44px;border-radius:50%;background:var(--lime);display:flex;align-items:center;justify-content:center}
.feature h5{position:absolute;left:57px;top:2px;font-size:8.4px;font-weight:400}
.feature p{position:absolute;left:57px;top:20px;width:186px;font-size:6.8px;line-height:12.5px;color:#333}
.feature a{position:absolute;left:57px;top:58px;font-size:6.9px;font-weight:600;color:var(--link);text-decoration:none}
.feature.ruled{border-bottom:1px solid #eee}
.footer{left:0;top:978px;width:814px;height:184px;background:var(--footer)}
.footer h6{position:absolute;top:29px;font-size:10.5px;font-weight:400;color:var(--sky)}
.footer ul{position:absolute;left:117px;top:60px;list-style:none}
.footer li{font-size:6.9px;line-height:12.8px;color:#444}
.addr{position:absolute;left:326px;display:flex;gap:10px;font-size:8px;line-height:12px;color:#333}
.addr svg{flex:none}
.news p{position:absolute;left:520px;top:60px;width:180px;font-size:6.9px;line-height:12.8px;color:#444}
.news .field{position:absolute;left:520px;top:108px;width:128px;height:30px;background:#fff;border:1px solid #ddd;font-size:7px;line-height:28px;padding-left:6px}
.news .go{position:absolute;left:648px;top:108px;width:51px;height:30px;background:var(--sky);color:#fff;font-size:10.5px;text-align:center;line-height:30px}
.bottom{left:0;top:1162px;width:814px;height:38px;background:var(--blue);color:#fff}
.bottom .copy{position:absolute;left:117px;top:14px;font-size:6.8px}
.bottom .social{position:absolute;left:404px;top:11px;display:flex;gap:7px}
.bottom .social span{width:13px;height:13px;border-radius:50%;background:#fff}
.bottom .links{position:absolute;right:116px;top:14px;font-size:6.8px}
</style>
</head>
<body>

<header class="abs header">
  <div class="abs brand">BaySide Stays</div>
  <div class="abs contact-top">
    <div class="mail">
      <svg width="13" height="9" viewBox="0 0 13 9"><rect x=".5" y=".5" width="12" height="8" fill="none" stroke="#fff"/><path d="M.5 .5 6.5 5 12.5 .5" fill="none" stroke="#fff"/></svg>
      hello@baysidestays.example
    </div>
    <div class="phone">1.855.BAY.STAY</div>
    <div class="phone-num">(1.855.229.7829)</div>
  </div>
</header>

<nav class="abs nav">
  <div class="home">
    <svg width="17" height="14" viewBox="0 0 17 14"><path d="M8.5 0 17 7h-2.5v7h-4V9.5h-4V14h-4V7H0z" fill="#fff"/></svg>
  </div>
  <a style="left:190px">See Our Spots</a><span class="sep" style="left:286px"></span>
  <a style="left:301px">Franchise information</a><span class="sep" style="left:400px"></span>
  <a style="left:415px">Our Philosophy</a><span class="sep" style="left:489px"></span>
  <a style="left:501px">List Your Property</a><span class="sep" style="left:586px"></span>
  <a style="left:598px">Contact Us</a><span class="sep" style="left:649px"></span>
  <a style="left:662px">News</a>
</nav>

<section class="abs intro">
  <svg class="abs" style="left:117px;top:22px" width="11" height="15" viewBox="0 0 11 15"><path d="M5.5 14.5C2 10 .8 7.5.8 5.5a4.7 4.7 0 0 1 9.4 0c0 2-1.2 4.5-4.7 9z" fill="none" stroke="#a4c639" stroke-width="1.6"/><circle cx="5.5" cy="5.3" r="1.8" fill="#a4c639"/></svg>
  <h1>Find Your Spot!</h1>
  <p>Choose one of the locations below to begin your search</p>
  <div class="share">
    <span style="background:#3b5998"></span>
    <span style="background:#2aa3ef"></span>
    <span style="width:18px;background:#fff;border:1px solid #ccc"></span>
    <span class="count">8</span>
  </div>
</section>

<div class="abs tile" style="left:117px;top:227px"><div class="photo" role="img" aria-label="Photo of a white rental house on a lawn" style="background:linear-gradient(#7e9a5e,#4f7433)"><div class="label">Harbor House</div></div></div>
<div class="abs tile" style="left:318px;top:227px"><div class="photo" role="img" aria-label="Photo of a backyard pool" style="background:linear-gradient(#5d7a48,#3f6a55)"><div class="label">Willow Pool Rental</div></div></div>
<div class="abs tile" style="left:519px;top:227px"><div class="photo" role="img" aria-label="Photo of a waterfront picnic spot" style="background:linear-gradient(#5e86ad,#46693a)"><div class="label">Lingering Shore</div></div></div>
<div class="abs tile" style="left:117px;top:384px"><div class="photo" role="img" aria-label="Photo of a pool beside a house" style="background:linear-gradient(#4d7a6a,#4a7638)"><div class="label">Reeds Landing</div></div></div>
<div class="abs tile" style="left:318px;top:384px"><div class="photo" role="img" aria-label="Photo of a cottage porch" style="background:linear-gradient(#8ea39a,#5d6f67)"><div class="label">Porchlight Cottage</div></div></div>
<div class="abs tile join" style="left:519px;top:384px"><div class="photo" role="img" aria-label="Photo of a country lane">
  <h2>Join Our Team</h2>
  <p>Become a part of our franchise<br>with exciting oppurtunity and growth</p>
  <div class="btn">Get in touch</div>
</div></div>

<main class="abs panel">
  <div class="story">
    <h3>Ready to Discover your Next Spot?</h3>
    <h4>Explore... Experience... Enjoy</h4>
    <p>BaySide Stays Lorem ipsum dolor sit amet, consectetur adipiscing elit. Aliquam laoreet sodales lacinia. Curabitur ut purus tincidunt, iaculis elit a, eleifend augue. Phasellus blandit augue vel sollicitudin blandit. Lorem ipsum dolor sit amet, consectetur adipiscing elit. Aliquam laoreet sodales lacinia. Curabitur ut purus tincidunt, iaculis elit a, eleifend augue. Phasellus blandit augue vel sollicitudin blandit.</p>
    <p>BaySide Stays Lorem ipsum dolor sit amet, consectetur adipiscing elit. Aliquam laoreet sodales lacinia. Curabitur ut purus tincidunt, iaculis elit a, eleifend augue. Phasellus blandit augue vel sollicitudin blandit. Lorem ipsum dolor sit amet, consectetur adipiscing elit. Aliquam laoreet sodales lacinia. Curabitur ut purus tincidunt, iaculis elit a, eleifend augue. Phasellus blandit augue vel sollicitudin blandit.</p>
    <p>BaySide Stays Lorem ipsum dolor sit amet, consectetur adipiscing elit. Aliquam laoreet sodales lacinia. Curabitur ut purus tincidunt, iaculis elit a, eleifend augue. Phasellus blandit augue vel sollicitudin blandit. Lorem ipsum dolor sit amet, consectetur adipiscing elit. Aliquam laoreet sodales lacinia. Curabitur ut purus tincidunt, iaculis elit a, eleifend augue. Phasellus blandit augue vel sollicitudin blandit.</p>
    <div class="more">Read More</div>
  </div>
  <div class="divider"></div>

  <div class="signup">
    <h3>Sign up for last minute deals!</h3>
    <div class="field">Enter Your Email</div>
    <div class="go">Sign up</div>
  </div>

  <div class="feature ruled" style="top:136px">
    <div class="icon"><svg width="20" height="26" viewBox="0 0 20 26"><path d="M10 25C4 17 1.5 13 1.5 9a8.5 8.5 0 0 1 17 0c0 4-2.5 8-8.5 16z" fill="none" stroke="#fff" stroke-width="2.4"/><circle cx="10" cy="9" r="3" fill="#fff"/></svg></div>
    <h5>Know of a Hidden Gem</h5>
    <p>Lorem ipsum dolor sit amet, consectetur adipiscing elit. Aliquam laoreet sodales lacinia.</p>
    <a>Let us know about it!</a>
  </div>
  <div class="feature ruled" style="top:229px">
    <div class="icon"><svg width="24" height="22" viewBox="0 0 24 22"><ellipse cx="12" cy="16" rx="6" ry="5" fill="#fff"/><ellipse cx="4" cy="9" rx="2.4" ry="3" fill="#fff"/><ellipse cx="20" cy="9" rx="2.4" ry="3" fill="#fff"/><ellipse cx="8.5" cy="4" rx="2.4" ry="3" fill="#fff"/><ellipse cx="15.5" cy="4" rx="2.4" ry="3" fill="#fff"/></svg></div>
    <h5>Spot travels free!</h5>
    <p>Lorem ipsum dolor sit amet, consectetur adipiscing elit. Aliquam laoreet sodales lacinia.</p>
    <a>Find out more</a>
  </div>
  <div class="feature" style="top:322px">
    <div class="icon"><svg width="28" height="28" viewBox="0 0 28 28"><circle cx="14" cy="14" r="12" fill="none" stroke="#fff" stroke-width="2"/><path d="M14 7v7h5" fill="none" stroke="#fff" stroke-width="2"/></svg></div>
    <h5>Last Minute Deals</h5>
    <p>Lorem ipsum dolor sit amet, consectetur adipiscing elit. Aliquam laoreet sodales lacinia.</p>
    <a>View Last minute Deals</a>
  </div>
</main>

<footer class="abs footer">
  <h6 style="left:117px;top:31px">FRANCHISE INFORMATION</h6>
  <ul>
    <li>About BaySide Stays</li>
    <li>Why a BaySide Stays Franchise</li>
    <li>FAQ</li>
    <li>see Our Spots</li>
    <li>Franchise information</li>
    <li>Our Philosophy</li>
    <li>List Your Property</li>
    <li>Contact Us</li>
  </ul>

  <h6 style="left:326px">ADDRESS</h6>
  <div class="addr" style="top:60px">
    <svg width="11" height="16" viewBox="0 0 11 16"><path d="M5.5 15.5C2 11 .5 8 .5 5.5a5 5 0 0 1 10 0c0 2.5-1.5 5.5-5 10z" fill="#222"/><circle cx="5.5" cy="5.5" r="1.8" fill="#f6f6f6"/></svg>
    <div>BaySide Stays, 42 Harbor Lane<br>Oxford, MD</div>
  </div>
  <div class="addr" style="top:100px">
    <svg width="11" height="17" viewBox="0 0 11 17"><rect x=".8" y=".8" width="9.4" height="15.4" rx="1.5" fill="none" stroke="#222" stroke-width="1.6"/><rect x="2.5" y="3" width="6" height="9" fill="#222"/></svg>
    <div>Call us: 1.855.BAY.STAY<br>(1.855.229.7829)</div>
  </div>
  <div class="addr" style="top:140px">
    <svg width="15" height="11" viewBox="0 0 15 11"><rect width="15" height="11" fill="#222"/><path d="M0 0 7.5 6 15 0" fill="none" stroke="#f6f6f6" stroke-width="1.2"/></svg>
    <div>hello@baysidestays.example</div>
  </div>

  <div class="news">
    <h6 style="left:520px">NEWSLETTER</h6>
    <p>Excepteur sint occaecat cupidatat non proident, sunt in culpa qui officia deserunt mollit anim id est laborum.</p>
    <div class="field">Enter Email</div>
    <div class="go">Sign Up</div>
  </div>
</footer>

<div class="abs bottom">
  <div class="copy">Copyright © 2014 BaySide Stays . All rights reserved.</div>
  <div class="social"><span></span><span></span><span></span><span></span></div>
  <div class="links">Home &nbsp;| &nbsp;About &nbsp;| &nbsp;FAQ | &nbsp;Contact</div>
</div>

</body>
</html>
```